New Property development signage

large poster for a new development.
3 metres x 2 metres. To include the following.

Varnock Meadows
TO LET
LUXURY FULLY FURNISHED LARGE
2 AND 3 BED APARTMENTS
Tilwick Estates
362 4159
www.tilwickestates-example.com

Need this to be large simple writing with Tilwick estates logo on the bottom

Target Market(s)

High end rental property market

Industry/Entity Type

Real Estate Development

Colors
000000
cbcbcb
0555a3

Requirements
Must have
• Name of the development must be in a different font, classic style
Nice to have
• Light Grey background, blues for colours
Should not have
• anymore than 3 /4 colours

```html
<!DOCTYPE html>
<html lang="en">
<head>
<meta charset="utf-8">
<title>Varnock Meadows – To Let</title>
<link rel="stylesheet" href="https://fonts.googleapis.com/css2?family=Anton&family=Arimo:wght@700&family=Kalam:wght@400&family=Playfair+Display:wght@700&display=swap">
<style>
  :root {
    --brand-blue: #064f8e;
    --signal-red: #e2001a;
    --paper: #ffffff;
    --ink-white: #ffffff;
  }
  html, body {
    margin: 0;
    padding: 0;
    width: 1200px;
    height: 800px;
    overflow: hidden;
    background: var(--paper);
  }
  .sign {
    display: block;
    width: 1200px;
    height: 800px;
  }
  .band-top { fill: var(--brand-blue); }
  .band-middle { fill: var(--signal-red); }
  .band-bottom { fill: var(--paper); }
  .to-let {
    font-family: "Anton", "Oswald", sans-serif;
    font-size: 128px;
    fill: var(--signal-red);
    letter-spacing: 2px;
  }
  .development-name {
    font-family: "Playfair Display", "Times New Roman", serif;
    font-weight: 700;
    font-size: 190px;
    fill: var(--ink-white);
  }
  .offer-line {
    font-family: "Kalam", cursive;
    font-size: 58px;
    fill: var(--ink-white);
  }
  .phone {
    font-family: "Arimo", Arial, sans-serif;
    font-weight: 700;
    font-size: 132px;
    fill: var(--brand-blue);
  }
  .website {
    font-family: "Arimo", Arial, sans-serif;
    font-weight: 700;
    font-size: 46px;
    fill: var(--brand-blue);
  }
  .agent-mark { fill: var(--brand-blue); }
  .agent-name {
    font-family: "Arimo", Arial, sans-serif;
    font-weight: 700;
    font-size: 62px;
    fill: var(--brand-blue);
  }
</style>
</head>
<body>
<svg class="sign" viewBox="0 0 1200 800" xmlns="http://www.w3.org/2000/svg">
  <rect class="band-bottom" x="0" y="0" width="1200" height="800"/>
  <path class="band-middle" d="M0 345 Q600 395 1200 365 L1200 590 Q600 555 0 592 Z"/>
  <path class="band-top" d="M0 0 H1200 V365 Q600 395 0 345 Z"/>

  <text class="to-let" transform="translate(136,332) rotate(-90)" textLength="296" lengthAdjust="spacingAndGlyphs">TO LET</text>

  <text class="development-name" x="176" y="166" textLength="988" lengthAdjust="spacingAndGlyphs">VARNOCK</text>
  <text class="development-name" x="170" y="336" textLength="992" lengthAdjust="spacingAndGlyphs">MEADOWS</text>

  <text class="offer-line" x="600" y="455" text-anchor="middle">Luxury Fully Furnished Large</text>
  <text class="offer-line" x="575" y="537" text-anchor="middle">2 and 3 Bed Apartments</text>

  <text class="phone" x="113" y="702" textLength="585" lengthAdjust="spacingAndGlyphs">362 4159</text>
  <text class="website" x="115" y="768" textLength="588" lengthAdjust="spacingAndGlyphs">www.tilwickestates-example.com</text>

  <g class="agent-block">
    <rect class="agent-mark" x="745" y="640" width="60" height="60"/>
    <text class="agent-name" x="828" y="670">Tilwick</text>
    <text class="agent-name" x="828" y="738">Estates</text>
  </g>
</svg>
</body>
</html>
```